Dulwick Medical

Need smart and sleek business cards design for my medical distribution company. use logos attached.

add my details

Harriet Colbeck
Director/Sales Agent
harriet@dulwickmedical.com.au
0461 835 207

```html
<!DOCTYPE html>
<html lang="en">
<head>
<meta charset="utf-8">
<title>Dulwick Medical – Business Cards</title>
<link href="https://fonts.googleapis.com/css2?family=Montserrat:wght@400;500;700;800&display=swap" rel="stylesheet">
<style>
  :root {
    --bg: #2b2b2d;
    --navy: #1e2a5e;
    --navy-deep: #1a2452;
    --sky: #2a86c2;
    --white: #ffffff;
    --ink: #1f2a5c;
    --muted: #2f3440;
  }
  * { box-sizing: border-box; margin: 0; padding: 0; }
  html, body { width: 1200px; height: 875px; overflow: hidden; }
  body {
    background: var(--bg);
    font-family: "Montserrat", sans-serif;
    position: relative;
  }
  .card {
    position: absolute;
    top: 289px;
    width: 520px;
    height: 297px;
    border-radius: 16px;
    overflow: hidden;
  }
  .card--back { left: 40px; background: var(--navy); }
  .card--front { left: 640px; background: var(--white); }

  .brand {
    position: absolute;
    display: flex;
    align-items: center;
    gap: 10px;
    font-weight: 700;
    letter-spacing: 0.06em;
    line-height: 1.05;
    text-transform: uppercase;
  }
  .brand__mark { width: 30px; height: 30px; flex: none; }
  .card--back .brand {
    left: 50%; top: 50%;
    transform: translate(-50%, -50%);
    font-size: 30px;
    color: #23306d;
  }
  .card--back .brand__mark { width: 40px; height: 40px; background: #23306d; }
  .card--front .brand {
    left: 30px; top: 38px;
    font-size: 22px;
    color: var(--navy);
  }
  .card--front .brand__mark { background: var(--sky); }

  .holder {
    position: absolute;
    right: 28px; top: 30px;
    text-align: right;
    color: var(--ink);
  }
  .holder__name { font-weight: 800; font-size: 22px; }
  .holder__role { font-weight: 500; font-size: 11px; color: var(--muted); margin-top: 2px; }

  .contact {
    position: absolute;
    left: 30px; top: 160px;
    list-style: none;
    font-size: 12.5px;
    color: var(--muted);
  }
  .contact li { display: flex; align-items: center; gap: 8px; margin-bottom: 6px; }
  .contact svg { width: 13px; height: 13px; fill: var(--sky); flex: none; }

  .wave { position: absolute; left: 0; bottom: 0; width: 520px; height: 297px; }
</style>
</head>
<body>
  <section class="card card--back" aria-label="Card back">
    <div class="brand"><span class="brand__mark"></span><span>Dulwick<br>Medical</span></div>
  </section>

  <section class="card card--front" aria-label="Card front">
    <svg class="wave" viewBox="0 0 520 297" aria-hidden="true">
      <path d="M520 70 C470 170 340 190 200 215" fill="none" stroke="var(--sky)" stroke-width="9"/>
      <path d="M0 297 L0 265 C120 215 260 205 380 180 C450 160 500 130 520 80 L520 297 Z" fill="var(--navy)"/>
      <path d="M20 268 C140 220 270 212 385 188 C455 170 500 140 515 100" fill="none" stroke="var(--white)" stroke-width="1.5"/>
    </svg>

    <div class="brand"><span class="brand__mark"></span><span>Dulwick<br>Medical</span></div>

    <div class="holder">
      <p class="holder__name">Harriet Colbeck</p>
      <p class="holder__role">Director/Sales Agent</p>
    </div>

    <ul class="contact">
      <li>
        <svg viewBox="0 0 24 24"><path d="M6.6 10.8a15.1 15.1 0 0 0 6.6 6.6l2.2-2.2a1 1 0 0 1 1-.25 11.4 11.4 0 0 0 3.6.57 1 1 0 0 1 1 1V20a1 1 0 0 1-1 1A17 17 0 0 1 3 4a1 1 0 0 1 1-1h3.5a1 1 0 0 1 1 1c0 1.25.2 2.45.57 3.57a1 1 0 0 1-.25 1z"/></svg>
        <span>0461 835 207</span>
      </li>
      <li>
        <svg viewBox="0 0 24 24"><path d="M2 5h20v14H2z M3 6l9 7 9-7" /></svg>
        <span>harriet@dulwickmedical.com.au</span>
      </li>
    </ul>
  </section>
</body>
</html>
```